Orvex Panel Flyer

I need a flyer designed for our Orvex Panel software service. Basically most of the content that is on the website (orvexpanel.com.au) but I have uploaded a couple of source files as well. Please continue with this blue colour scheme

Target Market(s)

Business owners

Industry/Entity Type

Software

Font styles to use
Sans Serif

Colors
0456a4

Requirements
Must have
• Content from orvexpanel.com.au and similar theme

```html
<!DOCTYPE html>
<html lang="en">
<head>
<meta charset="utf-8">
<title>Orvex Panel Flyer</title>
<link rel="stylesheet" href="https://fonts.googleapis.com/css2?family=Oswald:wght@400;500&display=swap">
<style>
  :root {
    --brand-blue: #0a55a5;
    --pink: #c9508f;
    --purple: #7a4f9c;
    --violet: #5a4f9e;
    --teal: #6fdcc4;
    --white: #ffffff;
    --name-blue: #3ea3f2;
  }
  html, body {
    margin: 0;
    padding: 0;
    overflow: hidden;
    background: var(--brand-blue);
  }
  .flyer {
    position: relative;
    width: 848px;
    height: 1200px;
    overflow: hidden;
    background: var(--brand-blue);
    font-family: "Oswald", "Arial Narrow", sans-serif;
  }
  .band-artwork {
    position: absolute;
    inset: 0;
    clip-path: polygon(0 0, 100% 0, 100% 72%, 0 30%);
    background:
      radial-gradient(ellipse 260px 200px at 85% 6%, rgba(111, 220, 196, 0.75), rgba(111, 220, 196, 0) 70%),
      linear-gradient(160deg, rgba(122, 79, 156, 0.85) 0%, rgba(90, 79, 158, 0.8) 35%, rgba(201, 80, 143, 0.7) 75%, rgba(201, 80, 143, 0.45) 100%);
  }
  .headline-frame {
    position: absolute;
    left: 80px;
    top: 211px;
    width: 300px;
    height: 574px;
    border: 22px solid var(--white);
  }
  .headline {
    position: absolute;
    left: 115px;
    top: 252px;
    margin: 0;
    color: var(--white);
    font-weight: 500;
    font-size: 50px;
    line-height: 92px;
    letter-spacing: 8px;
  }
  .brand-name {
    position: absolute;
    left: 34px;
    top: 1072px;
    margin: 0;
    color: var(--name-blue);
    font-weight: 500;
    font-size: 46px;
    line-height: 1.1;
    letter-spacing: 1px;
  }
  .web-address {
    position: absolute;
    left: 324px;
    top: 1143px;
    margin: 0;
    color: var(--white);
    font-weight: 400;
    font-size: 17px;
    letter-spacing: 6px;
  }
</style>
</head>
<body>
<main class="flyer">
  <div class="band-artwork" role="img" aria-label="Decorative diagonal zigzag bands in pink, purple and teal across the upper area"></div>

  <div class="headline-frame"></div>
  <h1 class="headline">Keep your<br>finger on<br>the<br>pulse of<br>your<br>business.</h1>

  <p class="brand-name">Orvex Panel</p>
  <p class="web-address">HTTP://ORVEXPANEL.COM.AU/</p>
</main>
</body>
</html>
```